We are looking for a simple design that would be uplifting for
upscale drug addicts

MERIDIAN COLLECTIVE

PLEASE SEE THE LINK FOR TAG LINE AND CONTENT

thank you.

here is all the actual info we need and we want something like this...

http://files.qzr.lumtrabox.example/rest/objects/7c2910e4b557d81a93e40bd59fa644163fe2adf0899f?uid=bdf8e1b9b6f556b6b83c44471fdc79%2fproofs&expires=1482716603&signature=kT9PwLmQxZbVoNHLdtrtlmoGHQB%3d

The shape and colors don't have to be like what I posted it is only an example.

Target Market(s)

Harlow Row, internet and creative types, men, early 30's,
upwardly mobile, drug addicts

current site

brightkestrelway.example

now launching new name Meridian Collective

Industry/Entity Type

Drug

Requirements
Must have
• upscale look, great font
Should not have
• a corporate look but should not look like a clinic.

```html
<!DOCTYPE html>
<html lang="en">
<head>
<meta charset="utf-8">
<title>Meridian Collective – Business Card</title>
<link rel="stylesheet" href="https://fonts.googleapis.com/css2?family=Source+Sans+3:wght@400&display=swap">
<style>
  :root {
    --page: #ffffff;
    --card: #ffffff;
    --card-edge: #6b6b6b;
    --ink: #111111;
    --on-band: #ffffff;
    --band-light: #d872aa;
    --band-mid: #c8178a;
    --band-deep: #9c2389;
  }
  * { margin: 0; padding: 0; box-sizing: border-box; }
  html, body {
    width: 1200px;
    height: 758px;
    overflow: hidden;
    background: var(--page);
    font-family: "Source Sans 3", "Myriad Pro", Arial, sans-serif;
    color: var(--ink);
  }
  .card {
    position: absolute;
    left: 46px;
    top: 49px;
    width: 1108px;
    height: 658px;
    background: var(--card);
    border: 1px solid var(--card-edge);
    overflow: hidden;
  }
  .brand-band {
    position: absolute;
    left: 0; top: 0;
    width: 100%;
    height: 245px;
    background: linear-gradient(90deg, var(--band-light) 0%, var(--band-mid) 48%, var(--band-deep) 100%);
    color: var(--on-band);
    text-align: center;
  }
  .brand-name {
    position: absolute;
    left: 0; right: 0;
    top: 72px;
    font-size: 52px;
    font-weight: 400;
    line-height: 1;
    letter-spacing: 0.2px;
    transform: translateX(-8px);
  }
  .tagline {
    position: absolute;
    left: 0; right: 0;
    top: 122px;
    font-size: 26px;
    line-height: 30px;
    transform: translateX(-8px);
  }
  .phones {
    position: absolute;
    left: 83px;
    top: 418px;
    font-size: 30px;
    line-height: 34px;
  }
  .contact {
    position: absolute;
    right: 90px;
    top: 358px;
    text-align: right;
  }
  .contact-name {
    font-size: 41px;
    line-height: 46px;
    letter-spacing: 0.2px;
  }
  .contact-role,
  .contact-address {
    font-size: 30px;
    line-height: 34px;
  }
  .contact-address { margin-right: 5px; }
  .email {
    position: absolute;
    left: 0; right: 0;
    top: 572px;
    text-align: center;
    font-size: 29px;
    line-height: 34px;
    transform: translateX(27px);
  }
  .accent-strip {
    position: absolute;
    left: 0; bottom: 0;
    width: 100%;
    height: 19px;
    background: linear-gradient(90deg, var(--band-light) 0%, var(--band-mid) 48%, var(--band-deep) 100%);
  }
</style>
</head>
<body>
  <div class="card">
    <header class="brand-band">
      <h1 class="brand-name">MERIDIAN COLLECTIVE</h1>
      <p class="tagline">Every step forward matters on the<br>road to your lasting recovery</p>
    </header>

    <div class="phones">
      <p>555 .014 .2290</p>
      <p>555 .014 .2291</p>
    </div>

    <div class="contact">
      <p class="contact-name">OWEN HALVERICK, CASAC</p>
      <p class="contact-role">Program Coordinator</p>
      <p class="contact-address">418 W. 87th St. Suite 302<br>NEW YORK, NY 10024</p>
    </div>

    <p class="email">counselor@harborlinehealth.example</p>

    <div class="accent-strip"></div>
  </div>
</body>
</html>
```